New Massage Business needs a Card design

We need a card design for our new massage therapy business based in Sydney, Au. The business is getting a makeover, so a little later on we'll need shirts, various pamphlets and promotional flyers, and possibly a website. The winner will be offered those jobs as well.

Colour scheme should be green, black, and steel/charcoal grey. The business focuses on massage as an anatomical solution to stress, muscle aches, pains and fatigue. Ideally we'd like an anatomical image of the muscle system (ref to the attached files). In my mind this image takes up most of the left third of the card, and shows points of tension and pain at the neck and lower back. This image should be the grey portion of the card.

On the upper right is the other image attached, with a simple line drawing of a vehicle on the left end of the line, and a building on the right end replacing the stick figure (we have a therapist specializing in mobile massage). The blank part in the middle of the line should have "Vital Bodyworks", and in smaller writing below, "The Tension Fix".

Bottom right corner should have the contact and business details.
On the back we'd like a "next appointment" and "refer a friend" option.

If you have a design which doesn't fit the above, but you feel suits the business, please submit anyway - sometimes you don't know what you like until you see it.

Business Details:
Name: Vital Bodyworks - The Tension Fix

Massage Therapy

Business Details:
Contact name: Marcus
Title: Massage Therapist
Contact: 0458203167
Email: info@qlbrelief.example

Requirements
Must have
• Colour scheme should be green, black, and steel/charcoal grey. The business focuses on massage as an anatomical solution to stress, muscle aches, pains and fatigue. Ideally we'd like an anatomical image of the muscle system (ref to the attached files). In my mind this image takes up most of the left third of the card, and shows points of tension and pain at the neck and lower back. This image should be the grey portion of the card.
• On the upper right is the other image attached, with a simple line drawing of a vehicle on the left end of the line, and a building on the right end replacing the stick figure (we have a therapist specializing in mobile massage). The blank part in the middle of the line should have "Vital Bodyworks", and in smaller writing below, "The Tension Fix".
• Bottom right corner should have the contact and business details.
• On the back we'd like a "next appointment" and "refer a friend" option.
Nice to have
• Matt finish - no gloss
• If you have a design which doesn't fit the above, but you feel suits the business, please submit anyway - sometimes you don't know what you like until you see it.
Should not have
• Anything 'Zen'. The business promotes the physiological and scientific benefits of massage. For clients with spiritual or meditative needs, we refer out.

```html
<!DOCTYPE html>
<html lang="en">
<head>
<meta charset="utf-8">
<title>Vital Bodyworks – Business Card</title>
<link rel="stylesheet" href="https://fonts.googleapis.com/css2?family=Open+Sans:wght@400;600&family=Great+Vibes&display=swap">
<style>
  :root {
    --canvas: #e9e8e4;
    --card-white: #f7f7f5;
    --green: #9cbd1f;
    --green-light: #b5d33a;
    --green-text: #8fbf22;
    --ink: #1e1e1e;
    --muscle-dark: #b9552f;
    --muscle-light: #e79a72;
    --silhouette: #1f2a1a;
    --shadow: rgba(0,0,0,.18);
  }
  * { margin: 0; padding: 0; box-sizing: border-box; }
  html, body { width: 1200px; height: 902px; overflow: hidden; }
  body {
    background: var(--canvas);
    font-family: "Open Sans", Arial, sans-serif;
    color: var(--ink);
    display: flex;
    flex-direction: column;
    align-items: center;
    justify-content: center;
    gap: 44px;
  }
  .card {
    position: relative;
    width: 640px;
    height: 366px;
    background: var(--card-white);
    box-shadow: 0 6px 18px var(--shadow);
    overflow: hidden;
  }
  .card-front__panel { position: absolute; inset: 0; }
  .card-front__anatomy {
    position: absolute;
    left: 56px; top: 22px;
    width: 190px; height: 322px;
    border-radius: 90px 90px 60px 60px;
    background: radial-gradient(ellipse at 50% 40%, var(--muscle-light), var(--muscle-dark));
    opacity: .85;
  }
  .card-front__brand {
    position: absolute;
    right: 28px; top: 26px;
    width: 250px;
    text-align: center;
  }
  .brand-name {
    font-weight: 400;
    font-size: 32px;
    line-height: 1.1;
    color: var(--ink);
    letter-spacing: .2px;
    white-space: nowrap;
  }
  .brand-tagline {
    font-size: 18px;
    line-height: 1.25;
    color: var(--ink);
    white-space: nowrap;
  }
  .card-front__person {
    position: absolute;
    left: 430px; top: 112px;
  }
  .person-name {
    font-family: "Great Vibes", cursive;
    font-size: 44px;
    line-height: 1;
  }
  .person-title { font-size: 14px; margin-top: 2px; white-space: nowrap; }
  .card-front__contact {
    position: absolute;
    left: 424px; top: 216px;
    width: 196px;
    font-size: 14px;
    font-style: normal;
    line-height: 1.5;
    text-align: center;
    white-space: nowrap;
  }
  .card-front__runners {
    position: absolute;
    right: 18px; bottom: 22px;
    width: 150px; height: 62px;
    background: linear-gradient(90deg, var(--silhouette), #2e3a25);
    border-radius: 30px 30px 8px 8px;
    opacity: .9;
  }
  .card-back {
    display: flex;
    flex-direction: column;
    align-items: center;
    justify-content: center;
  }
  .card-back .brand-name {
    color: var(--green-text);
    font-size: 52px;
  }
  .card-back .brand-tagline { font-size: 22px; }
</style>
</head>
<body>
  <section class="card card-front">
    <svg class="card-front__panel" width="640" height="366" viewBox="0 0 640 366" aria-hidden="true">
      <path d="M220,0 C420,80 440,270 330,366 L344,366 C454,270 434,80 234,0 Z" fill="var(--green-light)"/>
      <path d="M234,0 H640 V366 H344 C454,270 434,80 234,0 Z" fill="var(--green)"/>
    </svg>
    <div class="card-front__anatomy" role="img" aria-label="Anatomical illustration of a running figure showing the muscle system with highlighted tension points"></div>
    <div class="card-front__brand">
      <h1 class="brand-name">Vital Bodyworks</h1>
      <p class="brand-tagline">The Tension Fix</p>
    </div>
    <div class="card-front__person">
      <p class="person-name">Marcus</p>
      <p class="person-title">Massage Therapist</p>
    </div>
    <address class="card-front__contact">
      <p>0458203167</p>
      <p>info@qlbrelief.example</p>
    </address>
    <div class="card-front__runners" role="img" aria-label="Row of black running figure silhouettes in motion sequence"></div>
  </section>

  <section class="card card-back">
    <h2 class="brand-name">Vital Bodyworks</h2>
    <p class="brand-tagline">The Tension Fix</p>
  </section>
</body>
</html>
```